Business Cards for a small business advisory (business services)

Professional look. Same as would apply for a lawyer, accountant, or other financial services professional. Please use the logo colors

Target Market(s)

small business owners

Industry/Entity Type

Financial Servics

Contact Information for Business Card

Name: Gavin L. Whitmore, CAIA / Title: Business Advisor / Office #: (718) 294-7716 / Mobile #: (917) 382-5047 / Email: g.whitmore@clearfieldventurepartners.example / Web: www.clearfieldventurepartners.example

Font styles to use
Sans Serif

```html
<!DOCTYPE html>
<html lang="en">
<head>
<meta charset="utf-8">
<title>Clearfield Venture Partners – Business Cards</title>
<link href="https://fonts.googleapis.com/css2?family=Montserrat:wght@400;500;600;700&display=swap" rel="stylesheet">
<style>
  :root {
    --navy: #1a3866;
    --green: #8cc63f;
    --white: #ffffff;
    --page: #f1f2f4;
    --faint: #eceef5;
    --shadow: rgba(0, 0, 0, 0.35);
  }
  * { box-sizing: border-box; margin: 0; padding: 0; }
  html, body { width: 1200px; height: 1200px; overflow: hidden; }
  body {
    background: var(--page);
    font-family: "Montserrat", sans-serif;
    display: flex;
    align-items: center;
    justify-content: center;
    gap: 40px;
  }
  .card {
    position: relative;
    width: 540px;
    height: 309px;
    overflow: hidden;
    box-shadow: 12px 14px 18px var(--shadow);
  }

  /* Back */
  .card-back {
    background: var(--navy);
    color: var(--white);
  }
  .card-back .brand {
    position: absolute;
    top: 118px;
    left: 0;
    right: 0;
    display: flex;
    align-items: center;
    justify-content: center;
    gap: 12px;
  }
  .brand-dot {
    width: 22px;
    height: 22px;
    border-radius: 50%;
    background: var(--green);
    flex: none;
  }
  .card-back .brand-name {
    font-size: 30px;
    font-weight: 600;
    color: var(--white);
    letter-spacing: -0.3px;
  }
  .card-back .web {
    position: absolute;
    left: 0;
    right: 0;
    top: 246px;
    text-align: center;
    font-size: 12px;
    letter-spacing: 3.6px;
    font-weight: 400;
  }
  .card-back .rule {
    position: absolute;
    left: 100px;
    right: 100px;
    height: 1px;
    background: linear-gradient(90deg, transparent, rgba(255,255,255,0.85) 15%, rgba(255,255,255,0.85) 85%, transparent);
  }
  .card-back .rule-top { top: 236px; }
  .card-back .rule-bottom { top: 272px; }

  /* Front */
  .card-front { background: var(--white); color: var(--navy); }
  .decor-circle {
    position: absolute;
    right: -20px;
    top: 28px;
    width: 250px;
    height: 250px;
    border-radius: 50%;
    background: var(--faint);
  }
  .card-front .brand {
    position: absolute;
    top: 40px;
    left: 26px;
    display: flex;
    align-items: center;
    gap: 10px;
  }
  .card-front .brand-name {
    font-size: 22px;
    font-weight: 600;
    color: var(--navy);
    letter-spacing: -0.2px;
  }
  .name-band {
    position: absolute;
    top: 140px;
    left: 0;
    width: 282px;
    height: 28px;
    background: var(--green);
    color: var(--white);
    font-size: 16px;
    font-weight: 600;
    line-height: 28px;
    padding-left: 36px;
    white-space: nowrap;
  }
  .job-title {
    position: absolute;
    top: 175px;
    left: 37px;
    font-size: 12.5px;
    letter-spacing: 1px;
    font-weight: 500;
  }
  .contacts {
    position: absolute;
    top: 206px;
    left: 34px;
    list-style: none;
  }
  .contacts li {
    display: flex;
    align-items: center;
    gap: 14px;
    height: 27px;
    font-size: 12.5px;
    font-weight: 500;
  }
  .contact-icon { width: 17px; height: 17px; flex: none; }
  .bottom-rule {
    position: absolute;
    left: 0;
    right: 0;
    bottom: 10px;
    height: 1.5px;
    background: linear-gradient(90deg, rgba(26,56,102,0.3), var(--navy) 20%, var(--navy) 80%, rgba(26,56,102,0.3));
  }
</style>
</head>
<body>

  <section class="card card-back" aria-label="Card back">
    <div class="brand">
      <span class="brand-dot"></span>
      <span class="brand-name">Clearfield Venture Partners</span>
    </div>
    <span class="rule rule-top"></span>
    <p class="web">www.clearfieldventurepartners.example</p>
    <span class="rule rule-bottom"></span>
  </section>

  <section class="card card-front" aria-label="Card front">
    <div class="decor-circle"></div>
    <div class="brand">
      <span class="brand-dot"></span>
      <span class="brand-name">Clearfield Venture Partners</span>
    </div>
    <div class="name-band">GAVIN L. WHITMORE, CAIA</div>
    <p class="job-title">BUSINESS ADVISOR</p>
    <ul class="contacts">
      <li>
        <svg class="contact-icon" viewBox="0 0 20 20" aria-hidden="true">
          <circle cx="10" cy="10" r="10" fill="#8cc63f"/>
          <path d="M7 5.5c.6-.3 1 0 1.3.5l.7 1.4c.2.4 0 .8-.3 1.1l-.6.5c.5 1.2 1.5 2.2 2.7 2.7l.5-.6c.3-.3.7-.5 1.1-.3l1.4.7c.5.3.8.7.5 1.3-.4.9-1.3 1.5-2.3 1.3C8.9 13.6 6.4 11.1 5.9 7.9c-.2-1 .3-2 1.1-2.4z" fill="#fff"/>
        </svg>
        (718) 294-7716
      </li>
      <li>
        <svg class="contact-icon" viewBox="0 0 20 20" aria-hidden="true">
          <circle cx="10" cy="10" r="10" fill="#8cc63f"/>
          <rect x="7" y="4.5" width="6" height="11" rx="1" fill="none" stroke="#fff" stroke-width="1.4"/>
          <circle cx="10" cy="13.4" r="0.8" fill="#fff"/>
        </svg>
        (917) 382-5047
      </li>
      <li>
        <svg class="contact-icon" viewBox="0 0 20 20" aria-hidden="true">
          <circle cx="10" cy="10" r="10" fill="#8cc63f"/>
          <rect x="5" y="6.5" width="10" height="7" rx="0.8" fill="none" stroke="#fff" stroke-width="1.3"/>
          <path d="M5.3 7l4.7 3.6L14.7 7" fill="none" stroke="#fff" stroke-width="1.3"/>
        </svg>
        g.whitmore@clearfieldventurepartners.example
      </li>
    </ul>
    <span class="bottom-rule"></span>
  </section>

</body>
</html>
```